Bright Acorns Business Card Design

Bright Acorns - Cultivating Natural Play Spaces

Bright Acorns is a company that focuses on promoting the design, construction, consultation and support of natural, creative and organic play spaces for Early Childhood and learning environments.

We need a professional Business Card designed that is unique modern and creative. The Philosophy of the company is nostalgic so the business and will need to reflect this but also reflect that our ideas are modern and cutting edge.

The business card will need to be a talking point, by either having a unique size, quality and/or placement of logo or other quality.

I am more interested in using natural recycled paper, as this would reflect the philosophy of the company, but I open to seeing colour used creatively.
Updates

Hi Designers, Apologies, Could you please add www.brightacorns.com.au to the business card. Thanks very much.

Hi All, Thank you all for your submission thus far. Please note the fonts for used in the logo are: Ostrich Sans Black and Archer Semi Bold. If these could be considered for contact details, my name etc. Also please show the design on a recycled brown card if possible as this will be the type of card I will use when printing. Thanks so much.

Target Market(s)

Child Care Providers, Play Industry Professionals

Industry/Entity Type

Business

Contact Information for Business Card

Bright Acorns
Cultivating Natural Play Spaces
Marlene Okafor
0419 862 304
marlene@brightacorns.com.au

Font styles to use
Sans Serif

Requirements
Must have
• The Logo and the Details plus the below phrase
• Bright Acorns - Cultivating Natural Play Spaces
Nice to have
• A bit of colour, but not too much colour.
Should not have
• Not to have a white background, recycled brown card only

```html
<!DOCTYPE html>
<html lang="en">
<head>
<meta charset="utf-8">
<title>Bright Acorns Business Card Design</title>
<link rel="stylesheet" href="https://fonts.googleapis.com/css2?family=Open+Sans:wght@400;600;700&display=swap">
<style>
  :root {
    --backdrop: #3b3431;
    --card: #141414;
    --card-edge: #0a0a0a;
    --ink: #f4f4f2;
    --ink-soft: #cfcfcc;
    --rule: #8a8a88;
  }
  * { box-sizing: border-box; margin: 0; padding: 0; }
  html, body {
    width: 1200px;
    height: 814px;
    overflow: hidden;
    background: var(--backdrop);
    font-family: "Open Sans", sans-serif;
    color: var(--ink);
  }
  .stage {
    position: relative;
    width: 1200px;
    height: 814px;
  }
  .card {
    position: absolute;
    top: 257px;
    width: 520px;
    height: 300px;
    background: var(--card);
    border: 1px solid var(--card-edge);
    box-shadow: 0 10px 24px rgba(0, 0, 0, 0.45);
  }
  .card--front { left: 50px; }
  .card--back { left: 630px; }

  /* Front */
  .brand {
    position: absolute;
    top: 46px;
    left: 0;
    right: 0;
    text-align: center;
  }
  .brand__mark {
    display: block;
    width: 16px;
    height: 16px;
    margin: 0 auto 10px;
    border-radius: 50%;
    background: var(--ink);
  }
  .brand__name {
    font-weight: 700;
    font-size: 30px;
    letter-spacing: 1.5px;
    text-transform: uppercase;
    line-height: 1.1;
  }
  .brand__tagline {
    margin-top: 6px;
    font-size: 10.5px;
    font-weight: 600;
    letter-spacing: 2px;
    text-transform: uppercase;
    color: var(--ink-soft);
  }
  .person {
    position: absolute;
    left: 34px;
    bottom: 48px;
    text-align: right;
    width: 256px;
  }
  .person__name {
    font-weight: 700;
    font-size: 20px;
    line-height: 1.3;
  }
  .person__email {
    font-size: 15px;
    color: var(--ink-soft);
    line-height: 1.4;
  }
  .divider {
    position: absolute;
    left: 306px;
    bottom: 44px;
    width: 1px;
    height: 82px;
    background: var(--rule);
  }
  .contact {
    position: absolute;
    left: 322px;
    bottom: 80px;
    list-style: none;
  }
  .contact__item {
    display: flex;
    align-items: center;
    gap: 9px;
    font-size: 14px;
    line-height: 24px;
    color: var(--ink-soft);
  }
  .contact__icon {
    width: 13px;
    height: 13px;
    flex: none;
  }

  /* Back */
  .back-brand {
    position: absolute;
    top: 86px;
    left: 0;
    right: 0;
    text-align: center;
  }
  .back-brand__mark {
    display: block;
    width: 22px;
    height: 22px;
    margin: 0 auto 14px;
    border-radius: 50%;
    background: var(--ink);
  }
  .back-brand__name {
    font-weight: 700;
    font-size: 38px;
    letter-spacing: 2px;
    text-transform: uppercase;
  }
  .back-url {
    position: absolute;
    bottom: 52px;
    left: 0;
    right: 0;
    text-align: center;
    font-size: 13px;
    letter-spacing: 2.5px;
    color: var(--ink-soft);
  }
</style>
</head>
<body>
<main class="stage">
  <section class="card card--front" aria-label="Business card front">
    <header class="brand">
      <span class="brand__mark" aria-hidden="true"></span>
      <div class="brand__name">Bright Acorns</div>
      <div class="brand__tagline">Cultivating Natural Play Spaces</div>
    </header>

    <div class="person">
      <div class="person__name">Marlene Okafor</div>
      <div class="person__email">marlene@brightacorns.com.au</div>
    </div>

    <div class="divider" aria-hidden="true"></div>

    <ul class="contact">
      <li class="contact__item">
        <svg class="contact__icon" viewBox="0 0 24 24" aria-hidden="true">
          <path fill="currentColor" d="M6.6 10.8a15.1 15.1 0 0 0 6.6 6.6l2.2-2.2a1 1 0 0 1 1-.25 11.4 11.4 0 0 0 3.6.57 1 1 0 0 1 1 1V20a1 1 0 0 1-1 1A17 17 0 0 1 3 4a1 1 0 0 1 1-1h3.5a1 1 0 0 1 1 1c0 1.25.2 2.45.57 3.57a1 1 0 0 1-.25 1z"/>
        </svg>
        <span>0419 862 304</span>
      </li>
      <li class="contact__item">
        <svg class="contact__icon" viewBox="0 0 24 24" aria-hidden="true">
          <circle cx="12" cy="12" r="10" fill="currentColor"/>
          <path d="M2 12h20M12 2c3 3 3 17 0 20M12 2c-3 3-3 17 0 20" stroke="#141414" stroke-width="1.6" fill="none"/>
        </svg>
        <span>brightacorns.com.au</span>
      </li>
    </ul>
  </section>

  <section class="card card--back" aria-label="Business card back">
    <div class="back-brand">
      <span class="back-brand__mark" aria-hidden="true"></span>
      <div class="back-brand__name">Bright Acorns</div>
    </div>
    <div class="back-url">www.brightacorns.com.au</div>
  </section>
</main>
</body>
</html>
```